Banner dimension 1767 X 887 for Tovarelo website

Need one banner for our website www.tovarelo.com.au, The dimension of the banner should be 1767 x 887. Attached to this brief are two images that needs to be on that one banner, PLEASE DO NOT SEND SEPARATE BANNERS, both images on the same banner. Thanks

The banner should have the following message on it:

1.) " Take a further 40% off all stock" ( use code: TOVARELO. Ends 31/12/2015)
2.) " Kick back or kick it up a notch this Autumn in the most versatile pique striped polo shirts and Pinafore belt strap denim dress"

Target Market(s)

kids aged 5-12yrs

Requirements
Must have
• very playful

```html
<!DOCTYPE html>
<html lang="en">
<head>
<meta charset="utf-8">
<title>Tovarelo – Take a further 40% off all stock</title>
<link rel="stylesheet" href="https://fonts.googleapis.com/css2?family=Fredoka:wght@600;700&display=swap">
<style>
  :root {
    --cream: #fbf6a8;
    --cream-light: #fdfad0;
    --splash-green: #6fae3f;
    --splash-green-deep: #3f8a3a;
    --splash-pink: #e0546b;
    --splash-pink-deep: #c8374f;
    --navy: #333a86;
    --green: #1bb15a;
    --ink: #1f1f1f;
    --pill: #0d0d0d;
    --white: #ffffff;
  }
  * { margin: 0; padding: 0; box-sizing: border-box; }
  html, body { width: 1200px; height: 602px; overflow: hidden; }
  body { font-family: "Fredoka", "Arial Rounded MT Bold", sans-serif; }

  .banner {
    position: relative;
    width: 1200px;
    height: 602px;
    overflow: hidden;
    background:
      radial-gradient(ellipse 330px 420px at 40px 260px, var(--splash-green-deep) 0%, var(--splash-green) 45%, rgba(111,174,63,0) 100%),
      radial-gradient(ellipse 340px 430px at 1180px 250px, var(--splash-pink-deep) 0%, var(--splash-pink) 45%, rgba(224,84,107,0) 100%),
      linear-gradient(90deg, #d9e98a 0%, var(--cream) 30%, var(--cream-light) 50%, var(--cream) 70%, #f3c9a4 100%);
  }
  .floor {
    position: absolute;
    left: 0; right: 0; bottom: 0;
    height: 135px;
    background: linear-gradient(180deg, rgba(255,255,230,0.55) 0%, rgba(240,240,170,0.35) 100%);
  }

  .kid-photo { position: absolute; border-radius: 40px; }
  .kid-photo--boy {
    left: 30px; top: 60px; width: 330px; height: 490px;
    background: linear-gradient(180deg, #3b6b4a 0%, #2d4f3a 40%, #7f9fbd 65%, #b79c82 85%, #2a2a2a 100%);
    opacity: 0.85;
  }
  .kid-photo--girl {
    left: 905px; top: 45px; width: 260px; height: 510px;
    background: linear-gradient(180deg, #5a3b2c 0%, #f2efe9 22%, #3f6c94 40%, #4f7ea6 70%, #d8b79e 85%, #e06877 100%);
    opacity: 0.85;
  }

  .offer {
    position: absolute;
    left: 390px; top: 14px; width: 400px;
    text-align: center;
    text-transform: uppercase;
    line-height: 1;
  }
  .offer__lead {
    color: var(--navy);
    font-size: 50px; font-weight: 700;
    transform: rotate(-3deg);
  }
  .offer__amount {
    color: var(--green);
    font-size: 158px; font-weight: 700;
    margin-top: -2px;
    letter-spacing: -2px;
  }
  .offer__tail {
    color: var(--navy);
    font-size: 50px; font-weight: 700;
    margin-top: -16px;
    transform: rotate(-3deg);
  }

  .promo-code {
    position: absolute;
    left: 455px; top: 286px; width: 288px; height: 54px;
    background: var(--pill);
    color: var(--white);
    border-radius: 27px;
    display: flex; flex-direction: column; justify-content: center; align-items: center;
    font-size: 21px; font-weight: 600; line-height: 1.05;
    text-transform: uppercase;
  }

  .tagline {
    position: absolute;
    left: 340px; top: 372px; width: 500px;
    text-align: center;
    color: var(--ink);
    font-size: 27px; font-weight: 700; line-height: 1.02;
    text-transform: uppercase;
  }

  .product {
    position: absolute;
    font-weight: 700; text-transform: uppercase;
    line-height: 0.95;
    text-align: center;
  }
  .product--polo {
    left: 380px; top: 490px; width: 180px;
    color: var(--navy);
    font-size: 27px;
    font-style: italic;
  }
  .product--dress {
    left: 605px; top: 492px; width: 285px;
    color: var(--green);
    font-size: 28px;
  }
</style>
</head>
<body>
  <main class="banner">
    <div class="floor"></div>

    <div class="kid-photo kid-photo--boy" role="img" aria-label="Smiling boy in a green and black striped polo shirt and denim cargo shorts, balancing playfully on one leg"></div>
    <div class="kid-photo kid-photo--girl" role="img" aria-label="Smiling girl in a white t-shirt and a belt strap denim pinafore dress with pink sneakers"></div>

    <section class="offer">
      <p class="offer__lead">Take a further</p>
      <p class="offer__amount">40%</p>
      <p class="offer__tail">Off all stock</p>
    </section>

    <div class="promo-code">
      <span>Use code: TOVARELO</span>
      <span>Ends 31/12/2015</span>
    </div>

    <p class="tagline">Kick back or kick it up<br>a notch this summer<br>in the most versatile pique</p>

    <p class="product product--polo">Striped<br>Polo<br>Shirts</p>
    <p class="product product--dress">Pinafore<br>Belt strap<br>Denim dress</p>
  </main>
</body>
</html>
```